Occupational Therapist does home accessibility for disabled folks; needs business card design

We need a business card for a company in Portland, Oregon that specializes in making homes accessible, comfortable, and functional for people who are disabled or aging who would like to stay in THEIR home. Our medical background as Occupational Therapists allows us to translate the functional needs of the person into the recommendations for the design of the home remodel.

Target Market(s)

Elderly, children of elderly
People with disabilities, families of people with disabilities

Industry/Entity Type

Business

Contact Information for Business Card

Company name: Hearthova
Name: Karen Dwyer Lopez, OTR/L, CAPS, ECHM
Occupational Therapist, Home Modification & Accessibility Specialist
website: www.hearthovahomes.com
email: hearthovahomes@mailbright.com
phone: (503)418-2957
CCB #: 384517

Font styles to use
Sans Serif

Requirements
Must have
• My logo
• Easy to read font with contrasting background
• Please list the Services offered: Occupational Therapy, Home safety & accessibility assessments, Home modification consulting, project management
Nice to have
• Friendly, welcoming feel
Should not have
• Dark colored background

```html
<!DOCTYPE html>
<html lang="en">
<head>
<meta charset="utf-8">
<title>Hearthova Business Card</title>
<link href="https://fonts.googleapis.com/css2?family=Lato:wght@400;700&display=swap" rel="stylesheet">
<style>
  :root {
    --stage: #ece8e3;
    --paper: #ffffff;
    --ink: #3a3a3a;
    --ink-soft: #4a4a4a;
    --accent: #c0661f;
    --slate-light: #5a5a5a;
    --slate-dark: #3d3d3d;
  }
  * { box-sizing: border-box; margin: 0; padding: 0; }
  html, body { width: 1200px; height: 646px; overflow: hidden; }
  body {
    background: var(--stage);
    font-family: "Lato", Arial, sans-serif;
    color: var(--ink);
    position: relative;
  }
  .card {
    position: absolute;
    box-shadow: 0 4px 14px rgba(0,0,0,0.25);
    overflow: hidden;
  }
  /* Front */
  .card-front {
    left: 54px; top: 187px; width: 528px; height: 302px;
    background: var(--paper);
  }
  .brand-front {
    position: absolute; left: 50px; top: 133px;
    display: flex; align-items: center; gap: 10px;
  }
  .brand-mark { width: 22px; height: 22px; background: var(--accent); flex: none; }
  .brand-name {
    font-weight: 700; font-size: 33px; color: var(--ink); line-height: 1;
  }
  .divider {
    position: absolute; left: 253px; top: 74px; width: 1px; height: 155px;
    background: linear-gradient(to bottom, transparent, var(--accent) 15%, var(--accent) 85%, transparent);
  }
  .details { position: absolute; left: 264px; top: 74px; }
  .person-name { font-weight: 700; font-size: 17px; color: var(--accent); line-height: 1.2; }
  .credentials, .role { font-size: 12px; color: var(--ink-soft); line-height: 15.5px; }
  .contact-list { list-style: none; margin-top: 12px; }
  .contact-list li {
    display: flex; align-items: center; gap: 4px;
    font-size: 15px; line-height: 20px; color: var(--ink);
  }
  .contact-list svg { width: 12px; height: 12px; fill: var(--accent); flex: none; }
  .license { font-size: 11.5px; color: var(--ink); margin-top: 3px; }
  /* Back */
  .card-back {
    left: 609px; top: 189px; width: 525px; height: 297px;
    background: radial-gradient(ellipse at 50% 30%, var(--slate-light), var(--slate-dark) 80%);
  }
  .brand-back {
    position: absolute; left: 0; right: 0; top: 100px;
    display: flex; justify-content: center; align-items: center; gap: 14px;
  }
  .brand-back .brand-mark { width: 34px; height: 34px; }
  .brand-back .brand-name { color: #ffffff; font-size: 52px; }
  .services-band {
    position: absolute; left: 0; right: 0; top: 226px; height: 55px;
    background: var(--paper); text-align: center; padding-top: 4px;
  }
  .services-title { font-size: 12.5px; color: var(--accent); line-height: 15px; }
  .services-list { font-size: 12.5px; color: var(--ink); line-height: 15.5px; }
</style>
</head>
<body>
  <section class="card card-front">
    <div class="brand-front">
      <span class="brand-mark"></span>
      <span class="brand-name">Hearthova</span>
    </div>
    <div class="divider"></div>
    <div class="details">
      <h1 class="person-name">Karen Dwyer Lopez</h1>
      <p class="credentials">OTR/L, CAPS, ECHM</p>
      <p class="role">Occupational Therapist</p>
      <p class="role">Home Modification &amp; Accessibility Specialist</p>
      <ul class="contact-list">
        <li>
          <svg viewBox="0 0 24 24" aria-hidden="true"><path d="M6.6 10.8a15.1 15.1 0 0 0 6.6 6.6l2.2-2.2a1 1 0 0 1 1-.25 11.4 11.4 0 0 0 3.6.57 1 1 0 0 1 1 1V20a1 1 0 0 1-1 1A17 17 0 0 1 3 4a1 1 0 0 1 1-1h3.5a1 1 0 0 1 1 1c0 1.25.2 2.45.57 3.6a1 1 0 0 1-.25 1z"/></svg>
          (503) 418 2957
        </li>
        <li>
          <svg viewBox="0 0 24 24" aria-hidden="true"><path d="M2 5h20v14H2z"/><path d="M3 6l9 7 9-7" fill="none" stroke="#fff" stroke-width="1.6"/></svg>
          hearthovahomes@mailbright.com
        </li>
        <li>
          <svg viewBox="0 0 24 24" aria-hidden="true"><circle cx="12" cy="12" r="10"/><path d="M2 12h20M12 2c3 3 3 17 0 20M12 2c-3 3-3 17 0 20M4 7h16M4 17h16" fill="none" stroke="#fff" stroke-width="1.3"/></svg>
          www.hearthovahomes.com
        </li>
      </ul>
      <p class="license">CCB #: 384517</p>
    </div>
  </section>

  <section class="card card-back">
    <div class="brand-back">
      <span class="brand-mark"></span>
      <span class="brand-name">Hearthova</span>
    </div>
    <div class="services-band">
      <p class="services-title">Services we provide:</p>
      <p class="services-list">Occupational Therapy, Home safety &amp; accessibility assessments</p>
      <p class="services-list">Home modification consulting, Project management</p>
    </div>
  </section>
</body>
</html>
```